Re-style home page - eye-catching and unique design for social commerce website

We need a new concept design for TrindaMo's home page.
We don't want to make huge changes but creating a more professional and eye-catching style.

We need to look very serious like a professional services company and in the same time to look like a social network for e-commerce.

Our logo is very captive and you can use to creating something of harmonious.

This is a re-style and I'm excepted to see unique and fresh design like Clovaret.

Target Market(s)

e-commerce and social

Industry/Entity Type

Social

Number of Pages Required

1 page

Font styles to use
Serif
Sans Serif

Requirements
Must have
• An eye-catching result.
• Search bar with logo and Login How it works and business
• The slogan with login and signup.
• Footer links.
Nice to have
• I would like to open the home page and see only two clear ways:
• -Consumer
• --Search
• --The slogan
• --Login and Signup
• --How it works
• -Business
• --Go to Business area
• Background: City, Shopping.
Should not have
• Scrollbar style!

```html
<!DOCTYPE html>
<html lang="en">
<head>
<meta charset="utf-8">
<title>TrindaMo — Shop directly from your Profile</title>
<link rel="stylesheet" href="https://fonts.googleapis.com/css2?family=Roboto:wght@400;500;700&display=swap">
<style>
  :root {
    --sky-top: #2f5f96;
    --sky-mid: #3c5e86;
    --street-glow: #a5604a;
    --street-dark: #1e2a3e;
    --panel-light: #d9d6d2;
    --panel-warm: #b9a48a;
    --accent-pink: #c2355e;
    --tile: #2b2b2b;
    --tile-edge: #1a1a1a;
    --white: #ffffff;
    --search-icon: #3a8ee6;
    --social-blue: #1e3ac8;
    --social-blue-dark: #1a32ad;
  }
  * { box-sizing: border-box; margin: 0; padding: 0; }
  html, body { width: 1200px; height: 1155px; overflow: hidden; }
  body {
    position: relative;
    font-family: "Roboto", Arial, sans-serif;
    color: var(--white);
    background: var(--street-dark);
  }
  .city-backdrop {
    position: absolute; inset: 0;
    background:
      radial-gradient(ellipse 500px 300px at 1000px 1000px, rgba(220,120,80,.55), transparent 70%),
      radial-gradient(ellipse 400px 260px at 120px 980px, rgba(180,90,70,.45), transparent 70%),
      linear-gradient(180deg, var(--sky-top) 0%, var(--sky-mid) 45%, #4a4c5c 70%, var(--street-glow) 90%, #6a4a48 100%);
  }
  .search-bar {
    position: absolute; left: 397px; top: 52px; width: 405px; height: 54px;
    background: var(--white); display: flex; align-items: center;
  }
  .search-input {
    flex: 1; padding-left: 20px; font-size: 16px; color: #444;
  }
  .search-button {
    width: 58px; height: 100%; border-left: 1px solid #ddd;
    display: flex; align-items: center; justify-content: center;
  }
  .top-link {
    position: absolute; top: 117px; font-size: 14.5px; color: var(--white);
  }
  .top-link.how { left: 396px; }
  .top-link.login { right: 398px; top: 115px; }
  .brand {
    position: absolute; top: 166px; left: 0; width: 1200px; text-align: center;
    font-size: 58px; font-weight: 700; letter-spacing: -1px; color: var(--white);
    z-index: 2;
  }
  .hero-panel {
    position: absolute; left: 191px; top: 210px; width: 819px; height: 818px;
    background:
      linear-gradient(100deg, var(--panel-light) 0%, var(--panel-light) 35%, rgba(194,53,94,.45) 55%, var(--panel-warm) 70%, var(--accent-pink) 100%);
  }
  .hero-photo-veil {
    position: absolute; inset: 0;
    background: linear-gradient(180deg, rgba(0,0,0,.05), rgba(0,0,0,.15));
  }
  .headline {
    position: absolute; top: 260px; width: 1200px; text-align: center;
    font-size: 40px; font-weight: 400;
  }
  .feed-title {
    position: absolute; top: 344px; width: 1200px; text-align: center;
    font-size: 29px; font-weight: 400;
  }
  .category {
    position: absolute; width: 193px; height: 52px;
    background: var(--tile);
    border-bottom: 2px solid var(--tile-edge);
    box-shadow: 0 1px 2px rgba(0,0,0,.4);
    display: flex; align-items: center; justify-content: center; text-align: center;
    font-size: 14.4px; line-height: 1.3; text-transform: uppercase;
  }
  .category.strong { font-size: 16px; font-weight: 500; }
  .tagline {
    position: absolute; top: 868px; width: 1200px; text-align: center; font-size: 25px;
  }
  .social-login {
    position: absolute; left: 495px; top: 914px; width: 223px; height: 44px;
    background: var(--social-blue); display: flex; align-items: center;
  }
  .social-mark {
    width: 48px; height: 100%; background: var(--social-blue-dark);
    display: flex; align-items: center; justify-content: center;
  }
  .social-mark span { width: 16px; height: 16px; background: var(--white); }
  .social-label { padding-left: 14px; font-size: 15px; font-weight: 500; }
  .signup {
    position: absolute; top: 970px; width: 1200px; text-align: center; font-size: 21px;
  }
  .footer-links {
    position: absolute; top: 1083px; width: 1200px; text-align: center; font-size: 13px;
  }
  .footer-links span.sep { margin: 0 6px; }
</style>
</head>
<body>
  <div class="city-backdrop" role="img" aria-label="Blurred city street at dusk with tall buildings and light trails"></div>

  <div class="search-bar">
    <div class="search-input">Search here...</div>
    <div class="search-button">
      <svg width="28" height="28" viewBox="0 0 28 28" aria-hidden="true">
        <circle cx="11" cy="11" r="8" fill="none" stroke="var(--search-icon)" stroke-width="3"/>
        <line x1="17" y1="17" x2="25" y2="25" stroke="var(--search-icon)" stroke-width="3.5" stroke-linecap="round"/>
      </svg>
    </div>
  </div>
  <div class="top-link how">How it work / Business</div>
  <div class="top-link login">Login / Sign up</div>

  <div class="hero-panel" role="img" aria-label="Woman's arm holding a payment card and colourful shopping bags">
    <div class="hero-photo-veil"></div>
  </div>

  <div class="brand">TrindaMo</div>

  <h1 class="headline">Shop directly from your Profile</h1>
  <h2 class="feed-title">SETUP YOUR FEED</h2>

  <div class="category" style="left:302px;top:406px">Active Life</div>
  <div class="category" style="left:503px;top:406px">Arts &amp; Entertainment</div>
  <div class="category" style="left:706px;top:406px">Automotive</div>

  <div class="category" style="left:302px;top:468px">Beauti &amp; Spas</div>
  <div class="category strong" style="left:503px;top:468px">Education</div>
  <div class="category" style="left:706px;top:468px">Event Planning<br>&amp; Services</div>

  <div class="category strong" style="left:302px;top:530px">Financial Services</div>
  <div class="category" style="left:503px;top:530px">Food</div>
  <div class="category" style="left:706px;top:530px">Health &amp; Medical</div>

  <div class="category" style="left:302px;top:592px">Home Servies</div>
  <div class="category" style="left:503px;top:592px">Hotels</div>
  <div class="category" style="left:706px;top:592px">Local Services</div>

  <div class="category" style="left:302px;top:654px">Mass Media</div>
  <div class="category" style="left:503px;top:654px">Nightlife</div>
  <div class="category" style="left:706px;top:654px">Pets</div>

  <div class="category" style="left:302px;top:716px">Professional<br>Services</div>
  <div class="category" style="left:503px;top:716px">Public Services &amp;<br>Goverment</div>
  <div class="category" style="left:706px;top:716px">Real Estate</div>

  <div class="category strong" style="left:401px;top:779px">Restaurants</div>
  <div class="category strong" style="left:602px;top:779px">Shopping</div>

  <div class="tagline">Save Your Time. Live Better</div>

  <div class="social-login">
    <div class="social-mark"><span></span></div>
    <div class="social-label">Login with Linkora</div>
  </div>
  <div class="signup">Sign Up</div>

  <nav class="footer-links">
    About us<span class="sep">|</span>Blog<span class="sep">|</span>Business Jobs<span class="sep">|</span>Privacy<span class="sep">|</span>FAQ<span class="sep">|</span>Contacts
  </nav>
</body>
</html>
```